High-end construction company needs a business card design

We need a modern looking business card that draws people in, is memorable and looks so good people will want to sick it on their fridges.
On the first side what is needed are:
Logo
My name - Tomas Verbelk
Title - Managing Director
Website - www.kravel.co.uk
Email - tomas@kravel.co.uk
Telephone - 020 5194 6381
Mobile - 07845319027
On the back side was is needed is a list of all the services we provide:
-Kitchen Renovations
-Bathroom Renovations
-House Renovations
-Garage Conversions
-Extensions
-Loft Conversions
-Conservatories
-Carpentry
-Tiling
-Electrical
-Plumbing & Heating
-Bricklaying
-Landscaping
-Decorating
-Plastering
We would like the colours to be the same shades as on the logo with grey or black for the words.
Target Market(s)
Anyone who needs building work done
Contact Information for Business Card
This business card is for a construction company which strives to deliver excellent service and quality.
The look and feel of the card should represent this.
Requirements
Must have
- On the first side what is needed are:
Logo
My name - Tomas Verbelk
Title - Managing Director
Website - www.kravel.co.uk
Email - tomas@kravel.co.uk
Telephone - 020 5194 6381
Mobile - 07845319027
Nice to have
- Cool looking features

```html
<!DOCTYPE html>
<html lang="en">
<head>
<meta charset="utf-8">
<title>Kravel Construction Ltd – Business Card</title>
<link href="https://fonts.googleapis.com/css2?family=Montserrat:wght@400;500;700;800&display=swap" rel="stylesheet">
<style>
  :root {
    --bg: #d9d9d7;
    --card-white: #ffffff;
    --brand-green: #4b8f3f;
    --bright-green: #6cbd45;
    --bullet-green: #8fd36a;
    --ink: #3a3a3a;
    --on-green: #ffffff;
  }
  * { margin: 0; padding: 0; box-sizing: border-box; }
  html, body { width: 1200px; height: 801px; overflow: hidden; }
  body {
    background: var(--bg);
    font-family: "Montserrat", sans-serif;
    display: flex;
    align-items: center;
    justify-content: center;
    gap: 40px;
  }
  .card {
    width: 540px;
    height: 309px;
    position: relative;
    box-shadow: 0 6px 18px rgba(0,0,0,0.18);
  }

  /* Front side */
  .card-front {
    background: var(--card-white);
    display: flex;
    align-items: center;
    padding: 0 36px 0 40px;
  }
  .front-brand {
    width: 210px;
    color: var(--bright-green);
    font-weight: 800;
    text-transform: uppercase;
    line-height: 1.1;
  }
  .front-brand .brand-name { font-size: 40px; letter-spacing: 1px; display: block; }
  .front-brand .brand-sub { font-size: 12px; letter-spacing: 2.5px; display: block; margin-top: 4px; }
  .front-divider {
    width: 1.5px;
    height: 150px;
    background: var(--brand-green);
    margin: 0 26px 0 10px;
  }
  .contact-name {
    color: var(--brand-green);
    font-weight: 700;
    font-size: 20px;
    letter-spacing: 1px;
    text-transform: uppercase;
  }
  .contact-title {
    color: var(--ink);
    font-size: 12px;
    margin: 2px 0 16px;
  }
  .contact-list { list-style: none; }
  .contact-list li {
    display: flex;
    align-items: center;
    gap: 7px;
    font-size: 12px;
    color: var(--ink);
    margin-bottom: 4px;
  }
  .contact-list svg { width: 11px; height: 11px; fill: var(--bright-green); flex: none; }

  /* Back side */
  .card-back {
    background: var(--brand-green);
    color: var(--on-green);
    display: flex;
    flex-direction: column;
    align-items: center;
    padding: 46px 26px 0;
  }
  .back-brand {
    font-weight: 800;
    text-transform: uppercase;
    text-align: center;
    line-height: 1.05;
  }
  .back-brand .brand-name { font-size: 50px; letter-spacing: 2px; display: block; }
  .back-brand .brand-sub { font-size: 14px; letter-spacing: 3px; display: block; margin-top: 4px; }
  .services-heading {
    display: flex;
    align-items: center;
    width: 100%;
    gap: 14px;
    margin: 22px 0 12px;
    font-weight: 700;
    font-size: 15px;
    letter-spacing: 1px;
  }
  .services-heading::before,
  .services-heading::after {
    content: "";
    flex: 1;
    height: 1px;
    background: var(--bullet-green);
  }
  .services-list {
    list-style: none;
    text-align: center;
    font-size: 11.5px;
    line-height: 1.8;
  }
  .services-list .dot { color: var(--bullet-green); margin: 0 4px; }
</style>
</head>
<body>

  <section class="card card-front" aria-label="Business card front">
    <div class="front-brand">
      <span class="brand-name">Kravel</span>
      <span class="brand-sub">Construction Ltd</span>
    </div>
    <div class="front-divider"></div>
    <div class="contact">
      <h1 class="contact-name">Tomas Verbelk</h1>
      <p class="contact-title">Managing Director</p>
      <ul class="contact-list">
        <li><svg viewBox="0 0 24 24"><path d="M6.6 10.8a15.1 15.1 0 0 0 6.6 6.6l2.2-2.2a1 1 0 0 1 1-.25 11.4 11.4 0 0 0 3.6.57 1 1 0 0 1 1 1V20a1 1 0 0 1-1 1A17 17 0 0 1 3 4a1 1 0 0 1 1-1h3.5a1 1 0 0 1 1 1c0 1.25.2 2.45.57 3.57a1 1 0 0 1-.25 1z"/></svg>020 5194 6381</li>
        <li><svg viewBox="0 0 24 24"><path d="M7 1h10a2 2 0 0 1 2 2v18a2 2 0 0 1-2 2H7a2 2 0 0 1-2-2V3a2 2 0 0 1 2-2zm0 3v14h10V4z"/></svg>07845319027</li>
        <li><svg viewBox="0 0 24 24"><path d="M2 5h20v14H2zm2 2v.5l8 5 8-5V7z"/></svg>tomas@kravel.co.uk</li>
        <li><svg viewBox="0 0 24 24"><circle cx="12" cy="12" r="10"/></svg>www.kravel.co.uk</li>
      </ul>
    </div>
  </section>

  <section class="card card-back" aria-label="Business card back">
    <div class="back-brand">
      <span class="brand-name">Kravel</span>
      <span class="brand-sub">Construction Ltd</span>
    </div>
    <h2 class="services-heading">OUR SERVICES</h2>
    <ul class="services-list">
      <li>Kitchen Renovations<span class="dot">•</span>Bathroom Renovations<span class="dot">•</span>House Renovations<span class="dot">•</span>Extensions</li>
      <li>Garage Conversions<span class="dot">•</span>Loft Conversions<span class="dot">•</span>Conservatories<span class="dot">•</span>Carpentry<span class="dot">•</span>Electrical</li>
      <li>Plumbing &amp; Heating<span class="dot">•</span>Bricklaying<span class="dot">•</span>Landscaping<span class="dot">•</span>Decorating<span class="dot">•</span>Plastering<span class="dot">•</span>Tiling</li>
    </ul>
  </section>

</body>
</html>
```